Wren Vehicle Polishing (Mobile detail)

I need a business card made up. I'd like it to be different in some form, either raised, embossed, debossed, something cool that stands out. (preferably embossed text somewhere in it). I will be including the Initial png file. Let me know if you need the photoshop of adobe illustrator file to work with.

Information to be included: Text: XXX-XXX-XXXX Phone: XXX-XXX-XXXX Email: wrenpolishcrew@mailbox-demo.net Website: www.socialpage-demo.net/wrenpolishKTR Hours of operation: Mon - Fri 7:00AM to 8:00PM Sat - 10:00AM to 8:00PM

Target Market(s)

Mobile automotive detailing

Industry/Entity Type

Automotive

Contact Information for Business Card

Make it stand out with embossed lettering, I'd also like the background to be glossy black or matte, something that represents a shiny car, black preferred

Requirements
Must have
• A glossy background, or something.
• My logo, pick one of them that best fits your design.
Should not have
• White background,
• something that does not stand out.

```html
<!DOCTYPE html>
<html lang="en">
<head>
<meta charset="utf-8">
<title>Wren Vehicle Polishing – Business Card</title>
<link href="https://fonts.googleapis.com/css2?family=Audiowide&family=Open+Sans:wght@400;600&family=Russo+One&display=swap" rel="stylesheet">
<style>
  :root {
    --page: #2a2622;
    --card-black: #151617;
    --stripe: #222426;
    --orange: #f29a2e;
    --orange-line: #e8541c;
    --white: #f4f4f4;
    --grey-text: #8f9294;
    --panel-light: #c9cbcd;
    --panel-dark: #7d8184;
    --panel-text: #eef0f1;
  }
  * { margin: 0; padding: 0; box-sizing: border-box; }
  html, body { width: 1200px; height: 1023px; overflow: hidden; }
  body {
    background: var(--page);
    display: flex;
    flex-direction: column;
    align-items: center;
    justify-content: center;
    gap: 56px;
    font-family: "Open Sans", sans-serif;
  }
  .card {
    position: relative;
    width: 760px;
    height: 434px;
    border-radius: 6px;
    overflow: hidden;
    background:
      linear-gradient(115deg, rgba(255,255,255,0.10) 0%, rgba(255,255,255,0) 45%),
      repeating-linear-gradient(0deg, var(--card-black) 0 3px, var(--stripe) 3px 6px);
    box-shadow: 0 14px 30px rgba(0,0,0,0.55);
  }
  /* front */
  .brand-mark {
    position: absolute;
    left: 44px; top: 130px;
    width: 290px;
    display: flex;
    align-items: center;
    gap: 16px;
  }
  .brand-dot {
    flex: none;
    width: 46px; height: 46px;
    border-radius: 50%;
    background: var(--orange);
  }
  .brand-name {
    font-family: "Audiowide", sans-serif;
    font-size: 30px;
    line-height: 1.15;
    color: var(--orange);
  }
  .person {
    position: absolute;
    left: 370px; top: 34px;
  }
  .person-name {
    font-family: "Audiowide", sans-serif;
    font-size: 40px;
    letter-spacing: 2px;
    color: var(--orange);
    text-transform: uppercase;
    white-space: nowrap;
  }
  .person-role {
    font-size: 18px;
    color: var(--grey-text);
    text-align: right;
    margin-top: 0;
  }
  .contact {
    position: absolute;
    left: 370px; top: 128px;
    font-family: "Russo One", sans-serif;
    color: var(--white);
    white-space: nowrap;
  }
  .contact-number { font-size: 26px; letter-spacing: 3px; line-height: 1.3; }
  .contact-label { font-size: 14px; letter-spacing: 1px; color: var(--orange); margin-right: 8px; }
  .contact-line { font-size: 14px; letter-spacing: 0.5px; line-height: 1.55; }
  .contact-line:first-of-type { margin-top: 6px; }
  .address-panel { position: absolute; left: 0; top: 0; }
  .panel-text {
    position: absolute;
    right: 36px; bottom: 24px;
    text-align: right;
    font-size: 15px;
    line-height: 1.4;
    color: var(--panel-text);
    font-style: normal;
  }
  .hours { margin-top: 6px; font-weight: 600; }
  /* back */
  .card-back { display: flex; align-items: center; justify-content: center; }
  .card-back .brand-mark { position: static; width: auto; }
  .card-back .brand-dot { width: 70px; height: 70px; }
  .card-back .brand-name { font-size: 44px; }
</style>
</head>
<body>
  <section class="card card-front">
    <svg class="address-panel" width="760" height="434" viewBox="0 0 760 434" aria-hidden="true">
      <defs>
        <linearGradient id="panelMetal" x1="0" y1="0" x2="1" y2="1">
          <stop offset="0" stop-color="#c9cbcd"/>
          <stop offset="0.55" stop-color="#7d8184"/>
          <stop offset="1" stop-color="#5d6063"/>
        </linearGradient>
      </defs>
      <path d="M300 434 C 380 320, 540 260, 760 250 L760 434 Z" fill="url(#panelMetal)"/>
      <path d="M300 434 C 380 320, 540 260, 760 250" fill="none" stroke="#e8541c" stroke-width="5"/>
    </svg>

    <div class="brand-mark">
      <span class="brand-dot"></span>
      <span class="brand-name">Wren Vehicle Polishing</span>
    </div>

    <div class="person">
      <div class="person-name">Dale Mercer</div>
      <div class="person-role">Detailer</div>
    </div>

    <div class="contact">
      <div class="contact-number"><span class="contact-label">TEXT</span>0400 555 019</div>
      <div class="contact-number"><span class="contact-label">PHONE</span>0400 555 020</div>
      <div class="contact-line">wrenpolishcrew@mailbox-demo.net</div>
      <div class="contact-line">www.socialpage-demo.net/wrenpolishKTR</div>
    </div>

    <address class="panel-text">
      48 Example Road<br>
      Example, 4000 QLD, Australia
      <div class="hours">Mon – Fri 7:00AM to 8:00PM<br>Sat 10:00AM to 8:00PM</div>
    </address>
  </section>

  <section class="card card-back">
    <div class="brand-mark">
      <span class="brand-dot"></span>
      <span class="brand-name">Wren Vehicle Polishing</span>
    </div>
  </section>
</body>
</html>
```